Quillory Nest Business Card

I need a business card design. We are a collaborate online training company. Our colors are gray and green. Our website is QuilloryNest.com

I would like an area for a profile picture within the card

```html
<!DOCTYPE html>
<html lang="en">
<head>
<meta charset="UTF-8">
<title>Quillory Nest Business Card</title>
<link href="https://fonts.googleapis.com/css2?family=Lato:wght@400;700;900&display=swap" rel="stylesheet">
<style>
  :root {
    --slate: #2b3133;
    --green: #8cc63f;
    --ink: #1c1c1c;
    --paper: #ffffff;
    --backdrop: #e4e6e7;
    --photo-light: #b9b3ad;
    --photo-dark: #4a4a4c;
  }
  * { margin: 0; padding: 0; box-sizing: border-box; }
  html, body { width: 1200px; height: 900px; overflow: hidden; }
  body {
    background: var(--backdrop);
    font-family: 'Lato', sans-serif;
    position: relative;
  }
  .card {
    position: absolute;
    left: 250px;
    width: 700px;
    height: 400px;
    overflow: hidden;
    box-shadow: 0 6px 18px rgba(0,0,0,0.18);
  }
  .card-back { top: 30px; background: var(--slate); }
  .card-front { top: 470px; background: var(--paper); }

  .brand {
    display: flex;
    align-items: center;
    gap: 16px;
    font-weight: 900;
    letter-spacing: -1px;
  }
  .brand-dot {
    width: 54px; height: 54px;
    border-radius: 50%;
    background: var(--green);
    flex: none;
  }
  .card-back .brand {
    position: absolute;
    top: 120px; left: 0; right: 0;
    justify-content: center;
    font-size: 64px;
    color: var(--green);
  }
  .card-back .web {
    position: absolute;
    top: 268px; left: 0; right: 0;
    text-align: center;
    color: #e8ecec;
    font-size: 19px;
    letter-spacing: 2px;
  }

  .photo-area {
    position: absolute;
    left: 0; top: 30px;
    width: 290px; height: 300px;
    background: linear-gradient(170deg, var(--photo-light) 0%, #8d8580 45%, var(--photo-dark) 100%);
    border-radius: 0 140px 0 0;
  }
  .card-front .brand {
    position: absolute;
    top: 46px; left: 320px;
    font-size: 48px;
    color: var(--ink);
  }
  .brand-dot.small { width: 44px; height: 44px; }
  .details {
    position: absolute;
    right: 40px; top: 138px;
    text-align: right;
    color: var(--ink);
    font-size: 19px;
    line-height: 1.35;
  }
  .details .name { color: var(--green); font-size: 27px; }
  .details .role { color: var(--ink); font-size: 21px; }
  .details .contact-line { display: flex; justify-content: flex-end; align-items: center; gap: 10px; }
  .details svg { width: 18px; height: 18px; fill: var(--green); }
  .swoosh { position: absolute; left: 0; bottom: 0; width: 700px; height: 160px; }
  .card-front .web {
    position: absolute;
    right: 80px; bottom: 14px;
    color: #ffffff;
    font-size: 24px;
    letter-spacing: 1.5px;
  }
</style>
</head>
<body>

<section class="card card-back">
  <div class="brand"><span class="brand-dot"></span>Quillory Nest</div>
  <p class="web">www.quillorynest.com</p>
</section>

<section class="card card-front">
  <div class="photo-area" role="img" aria-label="Profile photo of the founder"></div>

  <div class="brand"><span class="brand-dot small"></span>Quillory Nest</div>

  <div class="details">
    <p><span class="name">Dorian Falk</span> <span class="role">Founder</span></p>
    <p>4870 W Marlow Ave. Suite 12</p>
    <p>Fenwick, Arizona 85390</p>
    <p class="contact-line">(302) 555-0147
      <svg viewBox="0 0 24 24" aria-hidden="true"><path d="M6.6 10.8a15.1 15.1 0 0 0 6.6 6.6l2.2-2.2a1 1 0 0 1 1-.25 11.4 11.4 0 0 0 3.6.57 1 1 0 0 1 1 1V20a1 1 0 0 1-1 1A17 17 0 0 1 3 4a1 1 0 0 1 1-1h3.5a1 1 0 0 1 1 1c0 1.25.2 2.45.57 3.57a1 1 0 0 1-.25 1z"/></svg>
    </p>
    <p class="contact-line">info@quillorynest.com
      <svg viewBox="0 0 24 24" aria-hidden="true"><path d="M2 5h20v14H2z M3.5 6.5 12 13l8.5-6.5" fill="none" stroke="#8cc63f" stroke-width="2"/></svg>
    </p>
  </div>

  <svg class="swoosh" viewBox="0 0 700 160" preserveAspectRatio="none" aria-hidden="true">
    <path d="M0 20 C 200 70, 420 130, 700 110 L700 160 L0 160 Z" fill="#2b3133"/>
    <path d="M0 8 C 180 40, 330 80, 470 120 C 330 90, 180 55, 0 24 Z" fill="#8cc63f"/>
  </svg>
  <p class="web">www.quillorynest.com</p>
</section>

</body>
</html>
```